pathology learning flashcard template graphic design .

Creative designs for 2 sides of the flashcards to include colorful sectioning and font sizes that will make it easy to use in studying.

```html
<!DOCTYPE html>
<html lang="en">
<head>
<meta charset="utf-8">
<title>Pathology Flashcard – Gastrointestinal</title>
<link href="https://fonts.googleapis.com/css2?family=Arvo:wght@400;700&family=Roboto:ital,wght@0,400;0,500;1,400;1,500&display=swap" rel="stylesheet">
<style>
  :root{
    --stage:#313330;
    --red:#d92c2c;
    --navy:#1a2166;
    --navy-mid:#2f4283;
    --periwinkle:#6580bd;
    --teal:#2ec4d0;
    --placeholder:#acd0cc;
    --heading-navy:#252f6e;
    --alert-red:#d83a2e;
    --answer-green:#1a9a5a;
    --body-ink:#333842;
    --white:#ffffff;
  }
  *{box-sizing:border-box;margin:0;padding:0}
  html,body{width:1200px;height:1200px;overflow:hidden}
  body{background:var(--stage);position:relative;font-family:'Roboto',sans-serif}

  .card{position:absolute;left:210px;width:780px;overflow:hidden}

  /* ---------- front ---------- */
  .card--front{top:61px;height:536px;background:var(--navy)}
  .front-header{position:absolute;left:0;top:0;width:100%;height:81px;background:var(--red);
    border-bottom:4px solid var(--white);display:flex;align-items:center;justify-content:center}
  .front-header h1{font-family:'Arvo',serif;font-weight:400;font-size:38px;letter-spacing:3px;color:var(--white);white-space:nowrap}
  .front-backdrop{position:absolute;left:0;top:85px;width:100%;height:451px;
    background:
      radial-gradient(ellipse 260px 220px at 360px 150px, rgba(150,60,130,.45), transparent 70%),
      radial-gradient(ellipse 320px 260px at 560px 250px, rgba(120,80,160,.35), transparent 70%),
      linear-gradient(90deg, var(--navy) 0%, var(--navy) 38%, #3a4f9c 62%, var(--periwinkle) 100%);}
  .case-id{position:absolute;left:37px;top:118px;width:417px;height:37px;background:var(--teal);
    font-family:'Arvo',serif;font-size:20px;letter-spacing:4px;color:var(--navy);white-space:nowrap;
    display:flex;align-items:center;padding-left:24px;overflow:hidden}
  .case-image{position:absolute;left:39px;top:184px;width:162px;height:162px;
    background:var(--placeholder);border:5px solid var(--white)}
  .case-text{position:absolute;left:230px;top:180px;width:517px;color:var(--white);
    font-size:16.6px;line-height:24.2px;text-align:justify}
  .case-text em{font-weight:500}
  .options{position:absolute;left:232px;top:418px;display:grid;grid-template-columns:175px auto;
    row-gap:5px;color:var(--white);font-size:17.4px;font-weight:500;line-height:24px;white-space:nowrap}

  /* ---------- back ---------- */
  .card--back{top:654px;height:535px;background:#eef2f8}
  .facts{position:absolute;left:0;top:0;width:390px;height:100%;
    background:linear-gradient(160deg,#f4f7fb 0%,#e3ebf4 55%,#eef1f7 100%)}
  .facts-title{height:62px;background:var(--navy-mid);padding-left:27px;display:flex;align-items:center}
  .facts-title h2{font-family:'Arvo',serif;font-weight:400;font-size:27px;letter-spacing:1.5px;color:var(--white)}
  .fact{position:absolute;left:29px;width:331px}
  .fact h3{font-family:'Arvo',serif;font-weight:400;font-size:18.2px;line-height:22px;color:var(--heading-navy);margin-bottom:5px;white-space:nowrap}
  .fact h3.alert{color:var(--alert-red)}
  .fact p{font-size:13px;line-height:17.3px;color:var(--body-ink);text-align:justify}

  .answer{position:absolute;left:390px;top:0;width:390px;height:100%}
  .answer-rx{position:absolute;left:0;top:0;width:100%;height:151px;
    background:linear-gradient(135deg,#dcf0f4 0%,#e8f5f6 60%,#dfe8ec 100%)}
  .answer-divider{position:absolute;left:0;top:151px;width:100%;height:5px;background:var(--teal)}
  .answer-key{position:absolute;left:0;top:156px;width:100%;height:270px;
    background:linear-gradient(160deg,#d6eef2 0%,#d9f0f1 60%,#cfe8ec 100%)}
  .answer-sources{position:absolute;left:0;top:425px;width:100%;height:110px;
    background:linear-gradient(160deg,#bcdcf3 0%,#9bcbee 55%,#86bde9 100%)}
  .answer h3{font-family:'Arvo',serif;font-weight:400;color:var(--heading-navy);white-space:nowrap}
  .answer p{color:var(--body-ink);text-align:justify}
  .rx{position:absolute;left:30px;top:27px;width:328px}
  .rx h3{font-size:17px;line-height:20px;margin-bottom:7px}
  .rx p{font-size:13.6px;line-height:19.4px}
  .key{position:absolute;left:30px;top:172px;width:328px}
  .key h3{font-size:21px;line-height:24px;color:var(--answer-green);margin-bottom:6px}
  .key p{font-size:13.6px;line-height:19.4px}
  .sources{position:absolute;left:30px;top:440px;width:328px;font-style:italic;color:var(--heading-navy)}
  .sources h4{font-weight:400;font-size:13.7px;margin-bottom:4px}
  .sources p{font-size:13px;line-height:17.4px;text-align:left;color:var(--heading-navy)}
</style>
</head>
<body>

<section class="card card--front">
  <header class="front-header"><h1>GASTROINTESTINAL</h1></header>
  <div class="front-backdrop" role="img" aria-label="Soft anatomical background of the digestive tract in blue and violet tones"></div>
  <div class="case-id">PATHOLOGY CASE ID 0001</div>
  <div class="case-image" role="img" aria-label="Case image placeholder"></div>
  <p class="case-text">50-year-old woman comes to the clinic because she has difficulty swallowing for the past few months. She says symptoms have been worsening. She also complains of cough, mostly at night and in fear of choking, has stopped eating many foods, losing about 12 lbs in the past 3 months. Past medical history is unremarkable. Vital signs are normal and physical exam is unremarkable. Chest x-ray with demonstrates an air-fluid level, while manometry shows absent relaxation of the lower esophageal sphincter during swallowing. <em>What is the most likely diagnosis?</em></p>
  <div class="options">
    <span>A) GERD</span><span>B) Barret Esophagus</span>
    <span>C) Achalasia</span><span>D) Eosinophilic esophagitis</span>
  </div>
</section>

<section class="card card--back">
  <div class="facts">
    <div class="facts-title"><h2>ACHALASIA</h2></div>
    <div class="fact" style="top:80px">
      <h3>Definition:</h3>
      <p>Motility disorder where esophageal relaxation is impaired in the lower esophageal sphincter (LES).</p>
    </div>
    <div class="fact" style="top:160px">
      <h3>Etiology/Pathology:</h3>
      <p>Destruction of inhibitory neurons in the Auerbach plexus. &nbsp;Loss of peristalsis in the lower esophageal sphincter (Lower-two thirds of the esophagus).</p>
    </div>
    <div class="fact" style="top:263px">
      <h3 class="alert">P/E and Symptoms:</h3>
      <p>Dysphagia that is progressive, regurgitation, weight-loss, dry cough, chest pain, GERD, esophageal perforation, squamous cell carcinoma, aspiration pneumonia.</p>
    </div>
    <div class="fact" style="top:366px;left:31px">
      <h3>Dx:</h3>
      <p>Barium swallow will show ‘bird’s beak’ and esophageal dilation. &nbsp;Manometry will present with increased resting lower esophageal sphincter pressure. Endoscopy will usually present with normal mucosa and LES dilation, and in some cases residual material such as undigested food particles may be present.</p>
    </div>
  </div>

  <div class="answer">
    <div class="answer-rx"></div>
    <div class="answer-divider"></div>
    <div class="answer-key"></div>
    <div class="answer-sources"></div>
    <div class="rx">
      <h3>Rx:</h3>
      <p>First line of treatment are nitrates, calcium channel blockers, and Botulinum toxin injection in the LES. Long term management options include esophageal dilation with pneumatic balloon and myotomy.</p>
    </div>
    <div class="key">
      <h3>C- Achalasia</h3>
      <p>Symptoms and studies suggestive of achalasia. Patient’s manometry presents with no relaxation of the lower esophageal sphincter during swallowing. Patient also complains of dysphagia and is unable to swallow properly, leading to weight loss. &nbsp;Patient has no past infection or inflammation, ruling out eosinophilic esophagitis. &nbsp;Patient does not have chronic GERD, eliminating the possibility of Barrett esophagus, in which at least 5 years of acid reflux are beforehand to develop columnar metaplasia.</p>
    </div>
    <div class="sources">
      <h4>Sources:</h4>
      <p>Harlow’s Drug Handbook; Pinewood Pocket Formulary; MedRefNet.com; ClinicalAtlas.com</p>
    </div>
  </div>
</section>

</body>
</html>
```